Velvet Meadow Custom Handmade Designs and more needs new business card

I am looking to get a new design for my business cards. My business is based in Baltimore, MD. The company is called “Velvet Meadow”. We offers a variety of products and services. The products include handmade earrings, phone cases, picture frame, hats, tutu’s, ect. You name it we make it. As well as a lipstick line called “Jinxa”. We also are a independent consultant for Lorna Belt and Odette Brim. Lastly, we offer make up services from our certified MUA. I know it seems like a lot but it works. It’s all thinks girly. Our company tag lines are “You name it, we make it!” and “Everyday is a fashion show and the world id your runway… are you ready?”. I would like the business cards to have a girly appeal to it. I would like it to have some sample pictures of what we do if possible. I am open to different ideas. If you want to see what we have, you can view my website. MyVelvetMeadow.com …. its not finished but it will give you an idea of everything. I have attached my new designed logos. There are 3 different types that you can choose from. If you need pictures, let me know of what. Thanks!

Target Market(s)

Wide market women of all ages

Industry/Entity Type

Business

Contact Information for Business Card

Name: Velvet Meadow ; Website: MyVelvetMeadow.com ; Number: 555-204-1938 ; Email: MyVelvetMdw@mailnest.net ; IG: Velvet_Mdw Pagebook.net/VelvetMeadow14 ; Craftly.net/Shop/MyVelvetMeadow

Font styles to use
Serif
Sans Serif
Decorative
Script

Requirements
Must have
• One of the logos (but you can change the colors if you like)
Nice to have
• Location: Woodlawn, MD ; Owner/ designer: Bianca Thorne ; Taglines: You Name it, we make it and/or Every day is a fashion show and the world is your runway… Are you ready?

```html
<!DOCTYPE html>
<html lang="en">
<head>
<meta charset="utf-8">
<title>Velvet Meadow – Business Card</title>
<link rel="stylesheet" href="https://fonts.googleapis.com/css2?family=Cabin:wght@400;600;700&family=Caveat:wght@500&family=Italianno&family=Oswald:wght@500&family=Roboto+Condensed:wght@400&display=swap">
<style>
  :root {
    --page: #e9e6e3;
    --ink: #121214;
    --black-card: #0b0b0d;
    --band: #2c2d2f;
    --band-light: #4a4b4d;
    --pink: #d0318f;
    --magenta: #c0238a;
    --violet: #9a4fb8;
    --white: #ffffff;
    --paper: #f4f4f5;
    --text-dark: #1c1c1c;
  }
  * { margin: 0; padding: 0; box-sizing: border-box; }
  html, body { width: 1200px; height: 1200px; overflow: hidden; }
  body {
    background: var(--page);
    font-family: "Cabin", Arial, sans-serif;
    position: relative;
  }
  .card {
    position: absolute;
    left: 190px;
    width: 820px;
    height: 470px;
    border-radius: 26px;
    overflow: hidden;
    box-shadow: 0 10px 28px rgba(0,0,0,0.25);
  }

  /* Front card */
  .card--front { top: 80px; background: var(--black-card); }
  .front__band {
    position: absolute;
    left: 0; right: 0; top: 140px; height: 200px;
    background: linear-gradient(90deg, var(--band-light) 0%, var(--band) 45%, #151517 46%, #0e0e10 100%);
  }
  .front__lips {
    position: absolute;
    left: 40px; top: 170px; width: 190px; height: 110px;
    border-radius: 50%;
    background: radial-gradient(ellipse at 40% 50%, var(--pink), var(--violet) 70%, transparent 72%);
  }
  .front__name {
    position: absolute;
    left: 240px; top: 188px;
    font-weight: 600;
    font-size: 72px;
    line-height: 1;
    color: var(--pink);
  }
  .front__tagline {
    position: absolute;
    left: 300px; top: 274px; width: 500px;
    font-family: "Caveat", cursive;
    font-size: 24px;
    line-height: 1.15;
    color: var(--white);
    text-align: center;
  }

  /* Back card */
  .card--back { top: 650px; background: linear-gradient(160deg, var(--white) 0%, var(--paper) 60%, #dedee0 100%); }
  .back__lips {
    position: absolute;
    left: 10px; top: 20px; width: 430px; height: 340px;
    border-radius: 50%;
    background: radial-gradient(ellipse at 45% 50%, var(--magenta) 0%, var(--pink) 40%, var(--violet) 66%, transparent 70%);
  }
  .back__info { position: absolute; left: 455px; top: 90px; width: 340px; }
  .back__name {
    font-weight: 600;
    font-size: 40px;
    color: var(--pink);
    line-height: 1;
    margin-left: 20px;
  }
  .back__services {
    margin-top: 18px;
    font-family: "Roboto Condensed", Arial, sans-serif;
    font-size: 24px;
    color: var(--text-dark);
    line-height: 1;
    white-space: nowrap;
  }
  .back__services-sub {
    font-family: "Caveat", cursive;
    font-size: 26px;
    color: var(--pink);
    line-height: 1.1;
    white-space: nowrap;
  }
  .back__owner { margin-top: 20px; margin-left: 20px; }
  .owner__name {
    font-family: "Italianno", cursive;
    font-size: 50px;
    line-height: 0.9;
    color: var(--ink);
  }
  .owner__title {
    font-family: "Oswald", Arial, sans-serif;
    font-size: 22px;
    letter-spacing: 2px;
    color: var(--pink);
    margin-left: 150px;
    line-height: 1;
  }
  .contacts { list-style: none; margin-top: 10px; }
  .contact {
    display: flex; align-items: center; gap: 12px;
    font-weight: 700;
    font-size: 19px;
    color: var(--text-dark);
    height: 38px;
    white-space: nowrap;
  }
  .contact svg { width: 30px; height: 30px; flex: none; }
</style>
</head>
<body>

  <section class="card card--front">
    <div class="front__band"></div>
    <div class="front__lips" role="img" aria-label="Pink glitter lipstick kiss mark logo"></div>
    <div class="front__name">Velvet Meadow</div>
    <p class="front__tagline">Everyday is a fashion show and the world is your runway…<br>Are you ready?</p>
  </section>

  <section class="card card--back">
    <div class="back__lips" role="img" aria-label="Large pink and violet lipstick kiss mark illustration"></div>
    <div class="back__info">
      <div class="back__name">Velvet Meadow</div>
      <p class="back__services">Multiple products and services</p>
      <p class="back__services-sub">available to match every personality</p>
      <div class="back__owner">
        <div class="owner__name">Bianca Thorne</div>
        <div class="owner__title">owner</div>
      </div>
      <ul class="contacts">
        <li class="contact">
          <svg viewBox="0 0 30 30" aria-hidden="true"><polygon points="15,1 28,8 28,22 15,29 2,22 2,8" fill="var(--pink)"/><rect x="9" y="13" width="12" height="7" rx="1.5" fill="#fff"/><path d="M8 12 Q15 6 22 12" stroke="#fff" stroke-width="2.4" fill="none"/><circle cx="15" cy="16.5" r="1.8" fill="var(--pink)"/></svg>
          555-204-1938
        </li>
        <li class="contact">
          <svg viewBox="0 0 30 30" aria-hidden="true"><polygon points="15,1 28,8 28,22 15,29 2,22 2,8" fill="var(--pink)"/><rect x="8" y="10" width="14" height="10" fill="#fff"/><path d="M8 10 L15 16 L22 10" stroke="var(--pink)" stroke-width="1.4" fill="none"/></svg>
          MyVelvetMdw@mailnest.net
        </li>
        <li class="contact">
          <svg viewBox="0 0 30 30" aria-hidden="true"><polygon points="15,1 28,8 28,22 15,29 2,22 2,8" fill="var(--pink)"/><circle cx="15" cy="15" r="6.5" fill="none" stroke="#fff" stroke-width="1.5"/><ellipse cx="15" cy="15" rx="2.8" ry="6.5" fill="none" stroke="#fff" stroke-width="1.2"/><line x1="8.5" y1="15" x2="21.5" y2="15" stroke="#fff" stroke-width="1.2"/></svg>
          MyVelvetMeadow.com
        </li>
      </ul>
    </div>
  </section>

</body>
</html>
```